business card design for velmora textile printing

Velmora Textile Printing requires elegant and colorful designs for its business card, ensuring both are visually cohesive and reflect the brand’s creative, modern identity. The logo is already finalized and should be a central element in designs.

## Business Card Design Brief

- Feature the logo clearly, with colors and style matching the letterhead.
- Present contact information (name, title, phone, email, website, address) in a clear, organized manner.
- Open to creative layouts, finishes, and double-sided designs, as long as the card remains professional and easy to read.
- Ensure both pieces feel unified as part of the same brand identity.

The final designs should be vibrant, professional, and memorable, showcasing Velmora Textile Printing’s creative spirit.

Target Market(s)

Pakistan

Industry/Entity Type

Textile printing

Other font styles liked:
• Calibri

Requirements
Must have
• Address Email Address Phone number designer can ask me when start designing

```html
<!DOCTYPE html>
<html lang="en">
<head>
<meta charset="utf-8">
<title>Velmora Textile Printing – Business Card</title>
<link rel="stylesheet" href="https://fonts.googleapis.com/css2?family=Carlito:wght@400;700&family=Montserrat:wght@500;600&display=swap">
<style>
  :root {
    --page-bg: #e9e2d8;
    --card-bg: #f3eee7;
    --card-edge: #fbf8f3;
    --brand-maroon: #5b1f26;
    --accent-orange: #e07a2b;
    --text-dark: #3a2f2a;
    --icon-orange: #d9652a;
    --art-orange: #f08a2a;
    --art-magenta: #d6286e;
    --art-purple: #7b2c8f;
  }
  html, body {
    margin: 0;
    padding: 0;
    width: 1200px;
    height: 1047px;
    overflow: hidden;
    background: var(--page-bg);
  }
  .canvas {
    position: relative;
    width: 1200px;
    height: 1047px;
  }
  .business-card {
    position: absolute;
    left: 80px;
    top: 240px;
    width: 1040px;
    height: 566px;
    border-radius: 26px;
    background: var(--card-bg);
    border: 2px solid var(--card-edge);
    box-shadow: 0 18px 40px rgba(80, 60, 40, 0.16);
    box-sizing: border-box;
    font-family: "Carlito", "Calibri", sans-serif;
  }
  .wordmark {
    position: absolute;
    left: 41px;
    top: 26px;
    margin: 0;
    font-family: "Montserrat", sans-serif;
    font-weight: 600;
    color: var(--brand-maroon);
    line-height: 1;
  }
  .wordmark-name {
    display: block;
    font-size: 76px;
    letter-spacing: 1px;
  }
  .wordmark-tagline {
    display: block;
    margin-top: 10px;
    margin-left: 6px;
    font-size: 28px;
    letter-spacing: 3.2px;
  }
  .person {
    position: absolute;
    left: 7px;
    top: 210px;
    height: 83px;
    padding-left: 38px;
    border-left: 14px solid var(--accent-orange);
  }
  .person-name {
    margin: 0;
    font-weight: 700;
    font-size: 42px;
    line-height: 1;
    letter-spacing: 0.5px;
    color: var(--accent-orange);
  }
  .person-title {
    margin: 8px 0 0;
    font-size: 27px;
    color: var(--text-dark);
  }
  .address {
    position: absolute;
    left: 45px;
    top: 322px;
    margin: 0;
    font-style: normal;
    font-size: 27px;
    line-height: 41px;
    color: var(--text-dark);
  }
  .contact-list {
    position: absolute;
    left: 45px;
    top: 422px;
    margin: 0;
    padding: 0;
    list-style: none;
    font-size: 27px;
    color: var(--text-dark);
  }
  .contact-item {
    display: flex;
    align-items: center;
    height: 40px;
  }
  .contact-icon {
    width: 20px;
    height: 20px;
    margin-right: 12px;
    fill: var(--icon-orange);
  }
  .brand-art {
    position: absolute;
    left: 432px;
    top: 36px;
    width: 570px;
    height: 497px;
  }
</style>
</head>
<body>
<main class="canvas">
  <section class="business-card">
    <h1 class="wordmark">
      <span class="wordmark-name">VELMORA</span>
      <span class="wordmark-tagline">TEXTILE PRINTING</span>
    </h1>

    <div class="person">
      <p class="person-name">FARID ANWAR</p>
      <p class="person-title">Managing Director</p>
    </div>

    <address class="address">Your address, City<br>State, Zip 1234</address>

    <ul class="contact-list">
      <li class="contact-item">
        <svg class="contact-icon" viewBox="0 0 20 20" aria-hidden="true"><path d="M2 7c0-2 3-4 8-4s8 2 8 4v1.5h-4V7H6v1.5H2z M5 10h10l2 7H3z"/></svg>
        123 456 789
      </li>
      <li class="contact-item">
        <svg class="contact-icon" viewBox="0 0 20 20" aria-hidden="true"><path d="M2 5h16v10H2z" /><path d="M2 5l8 6 8-6" fill="none" stroke="#f3eee7" stroke-width="1.6"/></svg>
        info@yourmail.com
      </li>
      <li class="contact-item">
        <svg class="contact-icon" viewBox="0 0 20 20" aria-hidden="true"><circle cx="10" cy="10" r="8"/><path d="M2 10h16M10 2c-3 3-3 13 0 16M10 2c3 3 3 13 0 16" fill="none" stroke="#f3eee7" stroke-width="1.3"/></svg>
        www.yourwebsite.com
      </li>
    </ul>

    <svg class="brand-art" viewBox="0 0 570 497" role="img" aria-label="Brand illustration area in orange, magenta and purple tones">
      <defs>
        <radialGradient id="artGlow" cx="45%" cy="55%" r="60%">
          <stop offset="0%" stop-color="var(--art-orange)" stop-opacity="0.85"/>
          <stop offset="50%" stop-color="var(--art-magenta)" stop-opacity="0.55"/>
          <stop offset="100%" stop-color="var(--art-purple)" stop-opacity="0"/>
        </radialGradient>
      </defs>
      <ellipse cx="285" cy="250" rx="285" ry="245" fill="url(#artGlow)"/>
    </svg>
  </section>
</main>
</body>
</html>
```